Research project presentation flyer

Pending approval of a cooperative research project we need a flyer to present and "market" the academic project to the businesses we want to invite to participate.

The project is a cooperation between three different universities and businesses in the Nordic/Baltic countries and the subject is innovation and entrepreneurship (see the attached "raw" edition).

The intended audience will be all those directly involved with the project, media, municipalities/government, businesses and also the public.

The flyer needs to be in multiple language-editions, but the design must of course be identical. For this designproject, we submit the English content (please correct the English in the attached proposal as necessary). Thus the project result must be in a format that allows us to replace the English text with other languages ourselves.

The proposal attached is just that: a laymans proposal (and the content). Please feel free to rearrange content (and redesign!)

The format of the flyer is a folded A4 (i.e. A5 portrait), with print on both sides.

The raw edition that is attached contains a map that is merely a suggestion (low quality). A better map - perhaps with less irrelevant detail - must be proposed. The important part of the map is to show the location of the universities and project office.

Also, the "logo" of the project is of low quality, and must be changed. A core concept of the project is "triple helix", so the "logo" of the project should be something to that effect (triple helix), as indicated. The "logo" is only an illustration to be used on the flyer. The aim is not to develop a logo for the project. We will do that at a later stage.

The flyer is supposed to be downloadable from a project web, both in hi-res for printing in a professional printshop, and for printing on an average office colour printer. Designs that bleeds off the paper-edge might therefore be a challenge, as office-printers don't print to the edge of the paper.

Reason: Due to Easter holiday and few submissons.

Target Market(s)

Industry/Entity Type

Printing

Requirements
Must have
• Format: A4 folded once, i.e. A5 portrait
Must be able to alter text in design to produce flyers in other languages that English (i.e. pdf is good for the English version, but editable fileformat must also be submitted)
Map must be improved
Logo must be improved. Concept: triple helix
Nice to have
• Clean, professional design.
Flyer is "selling" an academic project that must appeal to businesses

```html
<!DOCTYPE html>
<html lang="en">
<head>
<meta charset="utf-8">
<title>Triple Helix-concept</title>
<link rel="stylesheet" href="https://fonts.googleapis.com/css2?family=Comfortaa:wght@400&family=Carlito:ital,wght@0,400;1,400&display=swap">
<style>
  :root {
    --stage: #0b0b0b;
    --paper: #ffffff;
    --paper-shade: #d6d6d6;
    --accent-blue: #1aa3dc;
    --rule-gold: #e3d39c;
    --link-grey: #9a9a9a;
    --molecule-dark: #2a2a2a;
    --molecule-mid: #7a7a7a;
    --molecule-light: #e4e4e4;
  }
  * { margin: 0; padding: 0; box-sizing: border-box; }
  html, body {
    width: 1200px; height: 900px; overflow: hidden;
    background: var(--stage);
  }
  .flyer-page {
    position: absolute; left: 300px; top: 26px;
    width: 600px; height: 848px;
    background: linear-gradient(90deg, var(--paper) 0%, var(--paper) 68%, #f3f3f3 82%, var(--paper-shade) 100%);
    overflow: hidden;
    font-family: "Carlito", "Calibri", sans-serif;
    color: var(--accent-blue);
  }
  .page-title {
    position: absolute; left: 78px; top: 118px;
    font-family: "Comfortaa", sans-serif; font-weight: 400;
    font-size: 44px; letter-spacing: 0.5px; line-height: 1;
  }
  .title-rule {
    position: absolute; left: 78px; top: 216px;
    width: 446px; height: 3px; background: var(--rule-gold);
  }
  .intro-text {
    position: absolute; left: 78px; top: 249px; width: 446px;
    font-size: 15.6px; line-height: 20.5px; text-align: justify;
  }
  .source-link {
    position: absolute; left: 78px; top: 390px;
    font-size: 12.5px; color: var(--link-grey);
  }
  .elements-lead {
    position: absolute; left: 78px; top: 428px;
    font-size: 12.5px; font-style: italic;
  }
  .elements-list {
    position: absolute; left: 78px; top: 462px; width: 452px;
    list-style: none; font-size: 12.5px; font-style: italic; line-height: 17px;
    z-index: 2;
  }
  .elements-list li { display: flex; }
  .elements-list .item-number { width: 52px; flex: none; }
  .molecule-illustration {
    position: absolute; left: 0; top: 624px; width: 330px; height: 224px;
    background:
      radial-gradient(ellipse at 20% 60%, var(--molecule-dark) 0%, rgba(42,42,42,0) 45%),
      radial-gradient(ellipse at 60% 35%, var(--molecule-light) 0%, rgba(228,228,228,0) 55%),
      radial-gradient(ellipse at 75% 70%, var(--molecule-mid) 0%, rgba(122,122,122,0) 50%),
      radial-gradient(ellipse at 30% 25%, #bdbdbd 0%, rgba(189,189,189,0) 45%);
    z-index: 1;
  }
</style>
</head>
<body>
  <article class="flyer-page">
    <h1 class="page-title">Triple Helix-concept</h1>
    <div class="title-rule"></div>
    <p class="intro-text">Internationally, the symbolics of Triple Helix (taken from mathematic models in DNA research) has been introduced in the description of symbiosis processes within innovation – illustrating how organisms may interact with each other, influence on and change each others behavior. From the link below, the following statements have been extracted:</p>
    <p class="source-link">http://www.helixforum-example.org/the-triple-helix-concept.html</p>
    <p class="elements-lead">The triple Helix concept comprises three basic elements:</p>
    <ol class="elements-list">
      <li><span class="item-number">(1)</span><span>A more prominent role for the university in innovation, on a par with industry and government in a knowledge based society;</span></li>
      <li><span class="item-number">(2)</span><span>A movement toward collaborative relationship among the three major institutional spheres, in which innovation policy is increasingly an outcome of interaction rather than a prescription from government;</span></li>
      <li><span class="item-number">(3)</span><span>In addition to fulfilling their traditional functions, each institutional sphere also “takes the role of the other” performing new roles as well as their non-traditional function. Institutions taking non-traditional roles are viewed as major potential source of “innovation in innovation”.</span></li>
    </ol>
    <div class="molecule-illustration" role="img" aria-label="Ball-and-stick molecular structure illustration in black, grey and white"></div>
  </article>
</body>
</html>
```